Electrical contractor in San Diego county since 1988

Provide a company name/ logo for business cards and forms. Newer and more modern old card is attached. Color preference is black and orange. Simple and streamlined nothing too busy. I have also attached a card that represents the simplicity of what we are looking for.

Contractor

```html
<!DOCTYPE html>
<html lang="en">
<head>
<meta charset="utf-8">
<title>K. M. Electric Inc. – Business Card</title>
<link rel="stylesheet" href="https://fonts.googleapis.com/css2?family=Ubuntu:wght@300;400;500;700&display=swap">
<style>
  :root {
    --page-bg: #e6e6e6;
    --card-bg: #232323;
    --accent: #e8772a;
    --accent-soft: #f08a3c;
    --text-light: #d9d9d9;
    --text-white: #ffffff;
  }
  * { margin: 0; padding: 0; box-sizing: border-box; }
  html, body {
    width: 1200px; height: 1200px; overflow: hidden;
    background: var(--page-bg);
    font-family: "Ubuntu", sans-serif;
  }
  .business-card {
    position: absolute;
    left: 150px; top: 343px;
    width: 900px; height: 514px;
    background: var(--card-bg);
  }
  .name-band {
    position: absolute;
    left: 0; top: 210px;
    width: 470px; height: 42px;
    background: var(--accent);
    display: flex; align-items: center; justify-content: flex-end;
    padding-right: 22px;
    color: var(--text-white);
    font-size: 22px;
  }
  .name-band .person { font-weight: 700; letter-spacing: 0.5px; }
  .name-band .role { font-weight: 400; }
  .company-block {
    position: absolute;
    right: 140px; top: 96px;
    text-align: left;
    color: var(--accent);
  }
  .license { font-size: 15px; font-weight: 500; margin-left: 14px; }
  .company-name {
    font-size: 38px; font-weight: 400; letter-spacing: 1px;
    line-height: 1.1;
  }
  .tagline { font-size: 18px; font-weight: 400; margin-left: 4px; }
  .brand-dot {
    position: absolute;
    right: 40px; top: 108px;
    width: 84px; height: 84px; border-radius: 50%;
    background: var(--accent);
  }
  .contact-block {
    position: absolute;
    left: 462px; top: 270px;
    color: var(--text-light);
    font-size: 24px; line-height: 1.15;
  }
  .contact-line { display: flex; align-items: center; gap: 8px; }
  .contact-line.plain { padding-left: 0; }
  .contact-icon { width: 20px; height: 20px; flex: none; }
</style>
</head>
<body>
  <div class="business-card">
    <div class="name-band">
      <span class="person">DALE HARMON</span><span class="role">-President</span>
    </div>

    <div class="company-block">
      <div class="license">Lic. 804172</div>
      <div class="company-name">K. M. ELECTRIC INC.</div>
      <div class="tagline">Commercial-New &amp; Remodel</div>
    </div>
    <div class="brand-dot"></div>

    <div class="contact-block">
      <div class="contact-line plain">P.O. box 2274</div>
      <div class="contact-line plain">Ridgeview : CA 91980-0412</div>
      <div class="contact-line">
        <svg class="contact-icon" viewBox="0 0 20 20" aria-hidden="true">
          <circle cx="10" cy="10" r="10" fill="#e8772a"/>
          <path d="M6 7.5c0-1 1-1.5 1.6-1.5l1 2-1 .9c.5 1.2 1.3 2 2.5 2.5l.9-1 2 1c0 .6-.5 1.6-1.5 1.6C8.6 13 6 10.4 6 7.5z" fill="#fff"/>
        </svg>
        <span>(555) 014-2786</span>
      </div>
      <div class="contact-line">
        <svg class="contact-icon" viewBox="0 0 20 20" aria-hidden="true">
          <circle cx="10" cy="10" r="10" fill="#e8772a"/>
          <rect x="5.5" y="8" width="9" height="5" rx="1" fill="#fff"/>
          <rect x="7.5" y="5.5" width="5" height="3" fill="#fff"/>
        </svg>
        <span>014-3390</span>
      </div>
    </div>
  </div>
</body>
</html>
```